Folded Card for Business Coach
Cards for Harbor for Momentum
Project: Folded Card for Business Coach
Folded Card for Business Coach  - Consulting
Creative Brief
Modern
Gerald M. Finch II
Gerry
USA
gerry@harborformomentum.com
www.harborformomentum.com
"Front of Card" the Logo and Gerry Large. I will want it to be able to be slipped into a clear plastic name badge holder... Inside, top flap, is the Logo's Icon, Inside Bottom flap, the size components around the center diagram. Back is where the contact info goes.
Back is where the contact info goes. The logo was just finalized.

```html
<!DOCTYPE html>
<html lang="en">
<head>
<meta charset="utf-8">
<title>Harbor for Momentum — Stationery Set</title>
<link rel="stylesheet" href="https://fonts.googleapis.com/css2?family=Open+Sans:wght@400;700;800&display=swap">
<style>
:root{
  --backdrop:#3a3b3d;
  --backdrop-dark:#2a2b2d;
  --paper:#ffffff;
  --paper-soft:#eef0f2;
  --ink:#1f3a5f;
  --ink-soft:#5a6470;
  --rule:#e2e5e8;
  --orange:#f39a1e;
  --green:#7cbf3a;
  --blue:#2a7fc1;
  --navy:#1d4f7a;
}
*{box-sizing:border-box;margin:0;padding:0}
html,body{width:1200px;height:382px;overflow:hidden}
body{background:linear-gradient(180deg,var(--backdrop),var(--backdrop-dark));font-family:"Open Sans",Arial,sans-serif;color:var(--ink);position:relative}
.item{position:absolute;background:var(--paper)}
.brand{display:flex;align-items:center;gap:5px;font-weight:800;color:var(--ink);white-space:nowrap}
.brand .dot{border-radius:50%;background:var(--orange);flex:none}
.tiny{font-size:5px;color:var(--ink-soft);line-height:1.5}

/* logo presentation */
.logo-panel{position:absolute;left:12px;top:12px;width:324px;height:130px}
.logo-panel .brand{position:absolute;left:14px;top:40px;font-size:19px;color:#fff;gap:9px}
.logo-panel .brand .dot{width:36px;height:36px}
.logo-panel .owner{position:absolute;left:150px;top:80px;font-size:8px;color:#c9ccd0}

/* cards */
.card{width:150px}
.card .brand{font-size:8px}
.card .brand .dot{width:10px;height:10px}
.card-contact{left:12px;top:162px;height:66px;padding:9px 10px}
.card-contact .tiny{margin-top:6px;text-align:center}
.card-name{left:12px;top:237px;height:58px;padding:8px 10px}
.card-name .nick{font-size:17px;font-weight:800;margin-top:8px}
.card-tent{left:12px;top:300px;height:64px;padding:7px 10px;border-top:1px dashed #c9ccd0}
.card-tent .nick{font-size:17px;font-weight:800;margin-top:10px}
.card-mark{left:174px;top:162px;width:150px;height:66px;background:var(--paper-soft);display:flex;align-items:center;justify-content:center}
.card-mark .ring{width:44px;height:44px;border-radius:50%;background:radial-gradient(circle,var(--green),var(--blue))}
.card-parts{left:174px;top:237px;width:150px;height:58px;background:var(--paper-soft);display:flex;align-items:center;justify-content:space-around}
.card-parts .fill{width:42px;height:42px;border-radius:4px;background:linear-gradient(135deg,var(--orange),var(--green),var(--blue))}
.card-back{left:174px;top:300px;width:150px;height:64px;padding:12px 10px;text-align:center}
.card-back .who{font-size:7px;font-weight:700}

/* letterheads */
.letter{top:12px;width:220px;height:348px;padding:12px}
.letter .brand{font-size:8px}
.letter .brand .dot{width:11px;height:11px}
.letter .head-info{position:absolute;right:12px;top:12px;text-align:right}
.letter .watermark{position:absolute;left:35px;top:110px;width:150px;height:150px;border-radius:50%;background:radial-gradient(circle,rgba(124,191,58,.16),rgba(42,127,193,.07) 70%,transparent)}
.letter .foot{position:absolute;left:12px;right:12px;bottom:8px;text-align:center;border-top:1px solid var(--rule);padding-top:3px}
.letter-1{left:346px}
.letter-2{left:598px}

/* envelopes */
.envelope{left:840px;width:348px;overflow:hidden}
.env-flap{top:36px;height:112px}
.env-flap svg{position:absolute;left:0;top:0}
.env-flap .brand{position:absolute;left:118px;top:48px;font-size:10px}
.env-flap .brand .dot{width:13px;height:13px}
.env-plain{top:156px;height:72px;padding:10px 12px}
.env-plain .brand,.env-small .brand,.env-window .brand{font-size:8px}
.env-plain .brand .dot,.env-small .brand .dot,.env-window .brand .dot{width:10px;height:10px}
.env-window{top:236px;height:60px;padding:10px 12px}
.env-window .pane{position:absolute;left:150px;top:24px;width:120px;height:24px;border:1px solid #d9dde1;border-radius:3px}
.env-small{top:304px;width:180px;height:56px;padding:9px 10px}
.env-small .foot{position:absolute;left:10px;bottom:6px}
</style>
</head>
<body>

<section class="logo-panel">
  <div class="brand"><span class="dot"></span>Harbor for Momentum</div>
  <p class="owner">Gerald M. Finch II</p>
</section>

<article class="item card card-contact">
  <div class="brand"><span class="dot"></span>Harbor for Momentum</div>
  <p class="tiny">Gerald M. Finch II · Business Coach<br>555 014 0198<br>gerry@harborformomentum.com</p>
</article>

<article class="item card card-name">
  <div class="brand"><span class="dot"></span>Harbor for Momentum</div>
  <p class="nick">Gerry</p>
</article>

<article class="item card card-tent">
  <div class="brand"><span class="dot"></span>Harbor for Momentum</div>
  <p class="nick">Gerry</p>
</article>

<article class="item card-mark">
  <div class="ring" role="img" aria-label="Brand icon on the inside top flap"></div>
</article>

<article class="item card-parts">
  <div class="fill" role="img" aria-label="Icon component pieces"></div>
  <div class="fill" role="img" aria-label="Icon component pieces in colour tiles"></div>
</article>

<article class="item card-back">
  <p class="who">Gerald M. Finch II</p>
  <p class="tiny">555 014 0198<br>gerry@harborformomentum.com<br>www.harborformomentum.com</p>
</article>

<article class="item letter letter-1">
  <div class="brand"><span class="dot"></span>Harbor for Momentum</div>
  <p class="tiny head-info">555 014 0198<br>gerry@harborformomentum.com</p>
  <div class="watermark"></div>
  <p class="tiny foot">12 Harbor Lane, Easton USA · www.harborformomentum.com</p>
</article>

<article class="item letter letter-2">
  <div class="brand"><span class="dot"></span>Harbor for Momentum</div>
  <div class="watermark"></div>
  <p class="tiny foot">12 Harbor Lane, Easton USA · gerry@harborformomentum.com</p>
</article>

<article class="item envelope env-flap">
  <svg width="348" height="112" viewBox="0 0 348 112" aria-hidden="true">
    <path d="M0 0H348V22Q174 40 0 22Z" fill="var(--navy)"/>
    <path d="M0 22Q174 40 348 22" stroke="var(--blue)" stroke-width="2" fill="none"/>
  </svg>
  <div class="brand"><span class="dot"></span>Harbor for Momentum</div>
</article>

<article class="item envelope env-plain">
  <div class="brand"><span class="dot"></span>Harbor for Momentum</div>
</article>

<article class="item envelope env-window">
  <div class="brand"><span class="dot"></span>Harbor for Momentum</div>
  <div class="pane"></div>
</article>

<article class="item envelope env-small">
  <div class="brand"><span class="dot"></span>Harbor for Momentum</div>
  <p class="tiny foot">www.harborformomentum.com</p>
</article>

</body>
</html>
```